Healthcare patient advocacy company needs banner for conference booth

We need a banner to hang behind us in our booth at conferences. I would like something that prominently features our company name - brovint LLC. And also includes the following language: No employee should face medical debt alone. No Plan should be unrepresented. Expert advocacy and legal support from first bill to final resolution. The colors we use for our other materials are HEX 002C45, FECC73, 00C6CF, E0D5B9, 004C66. And the font is Epilogue. I would welcome some graphics, but no scales of justice or dollar bills or anything like that. I'm attaching some materials so you can see one of our brochures.

Target Market(s)

B2B - health insurers, third-party health care administrators, cost-containment companies

Industry/Entity Type

Healthcare Advocacy

Requirements
Must have
• Name prominently displayed and taglines in project description.
Nice to have
• I would like something easy to read and eye-catching that is not overly complicated or cutsey.
Should not have
• Scales of justice or dollar signs.

```html
<!DOCTYPE html>
<html lang="en">
<head>
<meta charset="utf-8">
<title>brovint LLC — Conference Booth Banner</title>
<link href="https://fonts.googleapis.com/css2?family=Epilogue:wght@400;600;700;800&display=swap" rel="stylesheet">
<style>
  :root {
    --stage: #b3b3b3;
    --navy: #1f2d6b;
    --teal: #00c6cf;
    --gold: #fecc73;
    --sky: #eef6fb;
    --deep: #0b1f2f;
    --ocean: #0a3f5e;
    --white: #ffffff;
  }
  * { box-sizing: border-box; margin: 0; padding: 0; }
  html, body {
    width: 706px; height: 1200px; overflow: hidden;
    background: var(--stage);
    font-family: "Epilogue", Arial, sans-serif;
  }
  .banner {
    position: absolute;
    left: 20px; top: 334px;
    width: 666px; height: 532px;
    overflow: hidden;
    background: var(--sky);
  }
  .banner-shapes {
    position: absolute; inset: 0;
    width: 100%; height: 100%;
  }
  .photo {
    position: absolute;
    left: 330px; top: 0;
    width: 336px; height: 532px;
    background:
      linear-gradient(90deg, var(--sky) 0%, rgba(238,246,251,0) 30%),
      linear-gradient(160deg, #e9ebed 0%, #d6d8da 45%, #c9b4a2 75%, #b9a08a 100%);
  }
  .brand-name {
    position: absolute;
    left: 0; right: 0; top: 30px;
    text-align: center;
    font-weight: 800;
    font-size: 42px;
    letter-spacing: -0.5px;
    color: var(--navy);
    line-height: 1;
  }
  .headline {
    position: absolute;
    left: 55px; top: 128px;
    font-weight: 800;
    font-size: 42px;
    line-height: 43px;
    letter-spacing: -1.2px;
    color: var(--navy);
    text-transform: uppercase;
  }
  .headline .accent { color: var(--teal); }
  .headline span { display: block; }
  .plan-tag {
    position: absolute;
    left: 56px; top: 306px;
    width: 287px; height: 27px;
    background: var(--navy);
    border-radius: 3px;
    color: var(--white);
    font-weight: 700;
    font-size: 13.5px;
    line-height: 29px;
    text-align: center;
    text-transform: uppercase;
    letter-spacing: -0.2px;
  }
  .plan-tag .highlight { color: var(--gold); }
  .support-copy {
    position: absolute;
    left: 55px; top: 345px;
    width: 300px;
    font-weight: 400;
    font-size: 14px;
    line-height: 18px;
    color: var(--navy);
  }
  .web-address {
    position: absolute;
    left: 0; right: 0; top: 483px;
    text-align: center;
    font-size: 19px;
    font-weight: 400;
    color: var(--white);
    line-height: 1;
  }
  .web-address strong { font-weight: 700; }
</style>
</head>
<body>
  <main class="banner">
    <div class="photo" role="img" aria-label="Photo of a doctor in a white coat with a stethoscope, writing on a clipboard"></div>

    <svg class="banner-shapes" viewBox="0 0 1189 950" preserveAspectRatio="none" aria-hidden="true">
      <defs>
        <linearGradient id="waveStripe" x1="0" y1="0" x2="1" y2="0">
          <stop offset="0" stop-color="#0b4a86"/>
          <stop offset="0.5" stop-color="#0a3d6a"/>
          <stop offset="1" stop-color="#00a3b8"/>
        </linearGradient>
        <linearGradient id="footerBase" x1="0" y1="0" x2="1" y2="0">
          <stop offset="0" stop-color="#0b1a28"/>
          <stop offset="1" stop-color="#0c4262"/>
        </linearGradient>
      </defs>
      <path d="M0 0 H1189 V78 Q595 268 0 83 Z" fill="#ffffff"/>
      <path d="M0 860 Q595 700 1189 840 V950 H0 Z" fill="url(#waveStripe)"/>
      <path d="M0 900 Q595 720 1189 895 V950 H0 Z" fill="#ffffff"/>
      <path d="M0 912 Q595 738 1189 912 V950 H0 Z" fill="url(#footerBase)"/>
    </svg>

    <h1 class="brand-name">brovint LLC</h1>

    <h2 class="headline">
      <span>No Employee</span>
      <span>Should Face</span>
      <span class="accent">Medical</span>
      <span class="accent">Debt Alone.</span>
    </h2>

    <p class="plan-tag">No plan should be <span class="highlight">unrepresented</span></p>

    <p class="support-copy">Expert advocacy and legal support from first bill to final resolution.</p>

    <p class="web-address">www.<strong>brovinthealth</strong>.com</p>
  </main>
</body>
</html>
```